Crestline Gas and Plumbing Business Card Design

I am after a business card design for my plumbing business called 'Crestline Gas & Plumbing'. I do all types of plumbing and gas work and specialise in general maintenance plumbing. Would like to see designs using current logo

Industry/Entity Type

Plumbing

Contact Information for Business Card

Name - Dale Whitcombe
Phone number - 0455163027
Email - admin@crestlinegasandplumbing.example.com.au
ABN - 68204915336

```html
<!DOCTYPE html>
<html lang="en">
<head>
<meta charset="utf-8">
<title>Crestline Gas &amp; Plumbing – Business Card</title>
<link rel="stylesheet" href="https://fonts.googleapis.com/css2?family=Montserrat:wght@800&family=Lato:wght@400;700&display=swap">
<style>
  :root {
    --stage: #2f2f31;
    --card-white: #ffffff;
    --brand-blue: #1a5fb4;
    --brand-orange: #f08a1c;
    --flame-yellow: #fcc312;
    --flame-orange: #f06a2c;
    --ink-grey: #3a3a3a;
    --rule-grey: #d4d4d4;
  }
  * { box-sizing: border-box; margin: 0; padding: 0; }
  html, body { width: 1200px; height: 896px; overflow: hidden; }
  body {
    background: var(--stage);
    display: flex;
    flex-direction: column;
    align-items: center;
    justify-content: center;
    gap: 32px;
  }
  .card {
    position: relative;
    width: 700px;
    height: 400px;
    overflow: hidden;
    box-shadow: 0 10px 28px rgba(0,0,0,.45);
  }

  /* Front */
  .card--front {
    background: var(--card-white);
    border-bottom: 10px solid var(--brand-orange);
  }
  .front__brand {
    position: absolute;
    right: 52px;
    top: 112px;
    text-align: left;
    font-family: "Montserrat", sans-serif;
    font-weight: 800;
    color: var(--brand-blue);
    line-height: 1;
  }
  .brand__name { font-size: 50px; letter-spacing: 1px; display: block; }
  .brand__tag { font-size: 17px; letter-spacing: 3px; display: block; margin-top: 6px; padding-left: 4px; }

  .front__contact {
    position: absolute;
    left: 52px;
    top: 214px;
    font-family: "Lato", sans-serif;
  }
  .contact__name {
    font-family: "Montserrat", sans-serif;
    font-weight: 800;
    font-size: 24px;
    letter-spacing: 1px;
    color: var(--brand-blue);
    margin-bottom: 10px;
  }
  .contact__line {
    display: flex;
    align-items: center;
    gap: 9px;
    font-size: 16px;
    color: var(--ink-grey);
    margin-top: 5px;
  }
  .contact__icon { width: 15px; height: 15px; flex: none; }

  .front__rule {
    position: absolute;
    left: 52px;
    right: 52px;
    top: 318px;
    height: 1px;
    background: var(--rule-grey);
  }
  .front__abn {
    position: absolute;
    right: 52px;
    top: 332px;
    font-family: "Lato", sans-serif;
    font-size: 17px;
    color: var(--ink-grey);
    letter-spacing: 1px;
  }
  .abn__label { color: var(--brand-orange); }

  /* Back */
  .card--back {
    background: linear-gradient(160deg, var(--flame-yellow) 0%, #f9a21e 45%, var(--flame-orange) 100%);
    display: flex;
    align-items: center;
    justify-content: center;
  }
  .back__flames {
    position: absolute;
    inset: 0;
    background: radial-gradient(ellipse at 85% 70%, rgba(255,255,255,.12), transparent 55%),
                radial-gradient(ellipse at 15% 20%, rgba(255,255,255,.10), transparent 50%);
  }
  .back__brand {
    position: relative;
    font-family: "Montserrat", sans-serif;
    font-weight: 800;
    color: var(--card-white);
    line-height: 1;
  }
  .back__brand .brand__name { font-size: 64px; }
  .back__brand .brand__tag { font-size: 22px; letter-spacing: 4px; }
</style>
</head>
<body>

  <section class="card card--front" aria-label="Business card front">
    <div class="front__brand">
      <span class="brand__name">CRESTLINE</span>
      <span class="brand__tag">GAS &amp; PLUMBING</span>
    </div>

    <div class="front__contact">
      <p class="contact__name">DALE WHITCOMBE</p>
      <p class="contact__line">
        <svg class="contact__icon" viewBox="0 0 16 16" aria-hidden="true">
          <path fill="#1a5fb4" d="M3.2 1.5l2.4 2.6-1.3 1.8c.9 2 2.6 3.7 4.6 4.6l1.8-1.3 2.6 2.4-1.5 2.2C6.6 13.6 2.4 9.4 1 4.2z"/>
        </svg>
        0455163027
      </p>
      <p class="contact__line">
        <svg class="contact__icon" viewBox="0 0 16 16" aria-hidden="true">
          <rect x="1" y="3" width="14" height="10" rx="1" fill="#1a5fb4"/>
          <path d="M1.5 3.5L8 9l6.5-5.5" fill="none" stroke="#fff" stroke-width="1.3"/>
        </svg>
        admin@crestlinegasandplumbing.example.com.au
      </p>
    </div>

    <div class="front__rule"></div>
    <p class="front__abn"><span class="abn__label">ABN -</span> 68204915336</p>
  </section>

  <section class="card card--back" aria-label="Business card back">
    <div class="back__flames" role="img" aria-label="Soft orange flame pattern background"></div>
    <div class="back__brand">
      <span class="brand__name">CRESTLINE</span>
      <span class="brand__tag">GAS &amp; PLUMBING</span>
    </div>
  </section>

</body>
</html>
```